Vessa Kliniq - Dermatology Consultation App

Vessa Kliniq is launching a new Pindle IOS App for online Dermatology consultation. We would appreciate a simple Scandinavian design which communicates trust, comfort and expensive feel. Most yacht designs have similar color palette, light wood colors and textures, but don’t be restricted by those in your artistic search.
The process is completed in three easy steps:
1. take a Snapshot.
2. Describe and Send it.
3. get Diagnosis and Treatment.
The Home screen should also have buttons - Start new Case, Follow up Visit, Rx Refill.
15% of the Home screen should also have a field/button - Medical Cosmetics Shop.
10% of the Home screen should also have a field or buttons for Our Partners (sponsors) – Lumavel, Norvexa, Toral, Ostra. (if you click you would be directed to their sites)
Note / Suggestion : Maybe you could use a larger picture of a dermatologist and have overlying fields and content, just for more influencing effect. (I am not a professional though)
Thank you so much.
24 - 59 Female
Club

```html
<!DOCTYPE html>
<html lang="en">
<head>
<meta charset="utf-8">
<title>Vessa Kliniq – App Screens</title>
<link rel="stylesheet" href="https://fonts.googleapis.com/css2?family=Montserrat:wght@300;400;500;600&display=swap">
<style>
  :root {
    --plum: #4b2b3c;
    --plum-soft: #5a3a4a;
    --ink: #3a3a3a;
    --muted: #6c6468;
    --line: #dfe3e8;
    --divider: #e6e6e8;
    --screen: #f7f7f8;
    --hero-a: #ffffff;
    --hero-b: #e4e2e5;
    --dot: #cfcfd3;
    --stage: #aab4bd;
  }
  * { box-sizing: border-box; margin: 0; padding: 0; }
  html, body { width: 1200px; height: 1100px; overflow: hidden; }
  body {
    background: var(--stage);
    font-family: "Montserrat", sans-serif;
    color: var(--ink);
    position: relative;
  }
  .screen {
    position: absolute;
    width: 430px;
    height: 760px;
    background: var(--screen);
    overflow: hidden;
    display: flex;
    flex-direction: column;
  }
  .screen--snapshot { left: 176px; top: 230px; z-index: 1; }
  .screen--message  { left: 384px; top: 163px; z-index: 2; }
  .screen--home     { left: 590px; top: 98px;  z-index: 3; }

  .status-bar {
    height: 32px;
    display: flex; align-items: center; justify-content: space-between;
    padding: 0 12px;
    font-size: 15px; font-weight: 500; color: var(--ink);
    background: #fff;
  }
  .status-bar .carrier { display: flex; align-items: center; gap: 4px; }
  .status-bar .signal { letter-spacing: -2px; font-size: 12px; margin-right: 4px; }
  .status-bar .battery { display: flex; align-items: center; gap: 6px; }
  .battery-icon { width: 28px; height: 13px; border: 1.5px solid var(--ink); border-radius: 3px; padding: 1px; }
  .battery-icon span { display: block; width: 62%; height: 100%; background: var(--ink); }

  .nav-bar {
    height: 60px;
    display: flex; align-items: center;
    padding: 0 12px;
    background: #fff;
    border-bottom: 3px solid var(--line);
    font-size: 17px; letter-spacing: .5px; color: var(--ink);
  }
  .nav-bar .back { display: flex; align-items: center; gap: 8px; width: 140px; }
  .nav-bar .title { flex: 1; text-align: center; font-weight: 500; font-size: 16.5px; }
  .nav-bar .search { width: 40px; display: flex; justify-content: flex-end; }

  .hero {
    height: 330px;
    background: radial-gradient(ellipse at 45% 35%, var(--hero-a) 0%, var(--hero-b) 100%);
    display: flex; flex-direction: column; align-items: center;
    position: relative;
  }
  .brand { display: flex; align-items: center; gap: 22px; margin-top: 66px; }
  .brand-mark { width: 150px; height: 150px; border: 2px solid var(--plum); border-radius: 50%; }
  .brand-name {
    font-size: 54px; line-height: 52px; font-weight: 500; color: var(--plum);
    letter-spacing: -1px;
  }
  .tagline {
    margin-top: 30px;
    font-size: 15.5px; font-weight: 500; letter-spacing: .4px; color: var(--plum);
  }
  .pager { display: flex; gap: 9px; position: absolute; bottom: 18px; }
  .pager i { width: 10px; height: 10px; border-radius: 50%; background: var(--dot); display: block; }
  .pager i.active { background: var(--plum); }

  .menu { background: #fff; margin: 0 5px; }
  .menu-item {
    height: 62px;
    display: flex; align-items: center; justify-content: space-between;
    padding: 0 18px;
    font-size: 23px; font-weight: 400; color: var(--muted);
    border-bottom: 1.5px solid var(--divider);
    letter-spacing: .2px;
  }
  .shop-row {
    height: 62px; margin: 0 5px;
    display: flex; align-items: center; justify-content: center;
    font-size: 23px; color: var(--muted); letter-spacing: .3px;
    background: #f1f1f3;
  }
  .partners {
    height: 62px; margin: 0 5px;
    background: var(--plum);
    display: flex; align-items: center; justify-content: space-around;
    padding: 0 14px;
    font-size: 20px; font-weight: 500; color: #fff; letter-spacing: .5px;
  }

  /* message screen */
  .message { background: #fff; padding: 24px 20px 0 22px; flex: 1; }
  .sender { display: flex; align-items: center; gap: 12px; }
  .avatar { width: 62px; height: 62px; border-radius: 50%; background: radial-gradient(circle, #6b6b6b, #1e1e1e); border: 3px solid #eee; }
  .sender-name { font-size: 21px; color: var(--ink); }
  .sender-date { font-size: 13px; color: var(--muted); margin-top: 2px; }
  .message-body { margin: 22px 0 0 26px; border-left: 6px solid var(--plum); padding-left: 20px; height: 410px; }
  .subject { font-size: 19px; margin-bottom: 14px; }
  .body-text { font-size: 14.5px; line-height: 21.5px; text-align: justify; }
  .sign-off { font-size: 14.5px; line-height: 21.5px; margin-top: 22px; padding-left: 4px; }
  .attachments { margin-top: 20px; font-size: 18.5px; font-weight: 500; display: flex; align-items: center; gap: 10px; }
  .attachment { font-size: 14.5px; display: flex; align-items: center; gap: 12px; margin: 10px 0 0 34px; }
  .message-actions {
    height: 60px; background: #efeff1;
    display: flex; align-items: center; gap: 50px; padding-left: 30px;
    font-size: 17px; color: var(--muted);
  }
  .message-actions span { display: flex; align-items: center; gap: 10px; }

  /* snapshot screen */
  .capture-area {
    height: 330px;
    background: radial-gradient(ellipse at 55% 40%, var(--hero-a) 0%, var(--hero-b) 100%);
    position: relative;
  }
  .capture-area .pager { left: 205px; bottom: 18px; }
</style>
</head>
<body>

<!-- Snapshot screen -->
<section class="screen screen--snapshot">
  <div class="status-bar">
    <span class="carrier"><span class="signal">●●●●●</span>Nordtel</span>
    <span>9:23 AM</span>
    <span></span>
  </div>
  <div class="nav-bar">
    <span class="back">‹&nbsp;BACK</span>
    <span class="title">TAKE A SNAPSHOT</span>
    <span class="search"></span>
  </div>
  <div class="capture-area" role="img" aria-label="Large camera shutter illustration">
    <div class="pager"><i></i><i></i><i></i><i></i><i></i></div>
  </div>
  <div class="menu">
    <div class="menu-item">NEW</div>
    <div class="menu-item">DELETE</div>
    <div class="menu-item">SEND</div>
  </div>
  <div class="shop-row">MEDICAL COSMETICS SHOP</div>
  <div class="partners"><span>Ostra</span><span>Toral</span><span>Lumavel</span><span>Norvexa</span></div>
</section>

<!-- Message screen -->
<section class="screen screen--message">
  <div class="status-bar">
    <span class="carrier"><span class="signal">●●●●●</span>Nordtel</span>
    <span>9:23 AM</span>
    <span></span>
  </div>
  <div class="nav-bar">
    <span class="back">‹&nbsp;BACK</span>
    <span class="title">SEND</span>
    <span class="search"></span>
  </div>
  <div class="message">
    <div class="sender">
      <div class="avatar" role="img" aria-label="Portrait photo of the patient"></div>
      <div>
        <div class="sender-name">From: Mira Holt</div>
        <div class="sender-date">10/03/2016</div>
      </div>
    </div>
    <div class="message-body">
      <div class="subject">Sub : Consultation</div>
      <p class="body-text">&nbsp;&nbsp;Lorem ipsum dolor sit amet, adipiscing elit. Aenean commodo scelerisque. Interdum et malesuada ante ipsum primis in faucibus. Donec vitae maximus lectus, sit amet consectetur justo, sed gravida bibendum ante.<br>&nbsp;&nbsp;Nam sit amet nisi id nulla tincidunt. Praesent at urna.</p>
      <div class="sign-off">Thanks,<br>&nbsp;&nbsp;&nbsp;Mira Holt</div>
      <div class="attachments">
        <svg width="22" height="22" viewBox="0 0 24 24" fill="none" stroke="currentColor" stroke-width="2"><path d="M20 11l-8.5 8.5a5 5 0 01-7-7L13 4a3.3 3.3 0 014.7 4.7l-8.4 8.4a1.7 1.7 0 01-2.4-2.4L14.5 7"/></svg>
        Attachments
      </div>
      <div class="attachment">
        <svg width="22" height="20" viewBox="0 0 24 22"><rect x="1" y="4" width="22" height="17" rx="3" fill="var(--plum)"/><rect x="7" y="1" width="10" height="5" rx="1" fill="var(--plum)"/><circle cx="12" cy="12.5" r="5" fill="#fff"/><circle cx="12" cy="12.5" r="3" fill="var(--plum)"/></svg>
        image_001.jpg
      </div>
      <div class="attachment">
        <svg width="22" height="20" viewBox="0 0 24 22"><rect x="1" y="4" width="22" height="17" rx="3" fill="var(--plum)"/><rect x="7" y="1" width="10" height="5" rx="1" fill="var(--plum)"/><circle cx="12" cy="12.5" r="5" fill="#fff"/><circle cx="12" cy="12.5" r="3" fill="var(--plum)"/></svg>
        image_002.jpg
      </div>
    </div>
  </div>
  <div class="message-actions">
    <span>
      <svg width="22" height="22" viewBox="0 0 24 24" fill="none" stroke="currentColor" stroke-width="2"><path d="M20 13v7H4V4h7"/><path d="M18 2l4 4-9 9H9v-4z"/></svg>
      Reply
    </span>
    <span>
      <svg width="26" height="22" viewBox="0 0 26 22" fill="none" stroke="currentColor" stroke-width="2"><path d="M20 14v6H2V7h5"/><path d="M8 15c1-6 6-8 12-8V3l5 5-5 5V9"/></svg>
      Forward
    </span>
  </div>
  <div class="partners"><span>Ostra</span><span>Toral</span><span>Lumavel</span><span>Norvexa</span></div>
</section>

<!-- Home screen -->
<section class="screen screen--home">
  <div class="status-bar">
    <span class="carrier"><span class="signal">●●●●●</span>Nordtel</span>
    <span>9:23 AM</span>
    <span class="battery">➤ 66% <span class="battery-icon"><span></span></span></span>
  </div>
  <div class="nav-bar">
    <span class="back">‹&nbsp;BACK</span>
    <span class="title">START SCREEN</span>
    <span class="search">
      <svg width="24" height="24" viewBox="0 0 24 24" fill="none" stroke="currentColor" stroke-width="2"><circle cx="10" cy="10" r="8"/><path d="M16 16l6 6"/></svg>
    </span>
  </div>
  <div class="hero">
    <div class="brand">
      <div class="brand-mark"></div>
      <div class="brand-name">Vessa<br>Kliniq</div>
    </div>
    <div class="tagline">ONLINE DERMATOLOGY CONSULTATION</div>
    <div class="pager"><i></i><i></i><i></i><i class="active"></i><i></i></div>
  </div>
  <div class="menu">
    <div class="menu-item">START NEW CASE</div>
    <div class="menu-item">FOLLOW UP VISIT</div>
    <div class="menu-item">RX REFILL
      <svg width="12" height="20" viewBox="0 0 12 20" fill="none" stroke="var(--ink)" stroke-width="2.5"><path d="M2 2l8 8-8 8"/></svg>
    </div>
  </div>
  <div class="shop-row">MEDICAL COSMETICS SHOP</div>
  <div class="partners"><span>Ostra</span><span>Toral</span><span>Lumavel</span><span>Norvexa</span></div>
</section>

</body>
</html>
```